High Profile Government Site Design

We need some concept designs for a website that will be used for reporting campaign contributions to politicians. I am including some images to give you an idea of what has been done so far. Basically the deliverable should be a landing page and perhaps a content page we can use to put in our charts and data tables. The landing page should be in a tiled format so we can list featured elections, show some general inforgraphical information, and offer a search capability. We do not want you to use the existing site design or logo in the images provided but to come up with your own concepts so we can share them with the committee that decides the final look. There is an existing site for this application located at http://apps.velmorstate.gov/apps/election/cfs/search/CandidateSearch.aspx . If you win there may be more work on this project and other projects.

Target Market(s)

Political

Industry/Entity Type

Government

Number of Pages Required

2 page

Font styles to use
Sans Serif

Colors

Designer to choose colors to be used in the design.

Requirements
Nice to have
• Some ideas are on the landing page offering up some segments for races of interest, contributors of interest, some statistical information, and potentially a search bar.
Should not have
• Should not use the current design or logo

```html
<!DOCTYPE html>
<html lang="en">
<head>
<meta charset="utf-8">
<title>Open Ledger — Campaign Finance</title>
<link href="https://fonts.googleapis.com/css2?family=Roboto:wght@300;400;500;700&display=swap" rel="stylesheet">
<style>
:root{
  --brand:#0c6f93;
  --nav:#17272e;
  --accent:#1fb5a8;
  --table-head:#12a0d8;
  --page:#f2f2f2;
  --card-line:#d4d4d4;
  --text:#333;
  --muted:#6b6b6b;
  --cyan:#4dd8f5;
  --blue:#5bb8da;
  --lilac:#b59fdc;
  --footer:#111;
}
*{box-sizing:border-box;margin:0;padding:0}
html,body{width:1085px;height:1200px;overflow:hidden}
body{position:relative;background:var(--page);font-family:'Roboto',sans-serif;color:var(--text)}
.site-header{position:absolute;left:0;top:0;width:1085px;height:84px;background:var(--brand)}
.brand{position:absolute;left:39px;top:16px;width:122px;height:57px;border:2px solid #fff;display:flex;align-items:center;justify-content:center;color:#fff;font-size:19px;font-weight:500;letter-spacing:1px}
.header-tools{position:absolute;right:70px;top:33px;display:flex;gap:13px}
.header-tools svg{width:16px;height:16px;fill:#fff}
.main-nav{position:absolute;left:0;top:84px;width:1085px;height:45px;background:var(--nav);display:flex;justify-content:space-between;padding:0 35px 0 49px;align-items:center}
.main-nav a{color:#fff;font-size:12px;text-decoration:none}
.nav-active{position:absolute;left:36px;top:84px;width:77px;height:3px;background:var(--accent)}
.hero{position:absolute;left:0;top:129px;width:1085px;height:355px;background:linear-gradient(90deg,#b88873 0%,#d9c6b8 30%,#a79b94 55%,#c7a48c 75%,#8d7f7a 100%)}
.search-panel{position:absolute;left:28px;top:310px;width:1029px;height:137px;background:rgba(255,255,255,.92);border:1px solid #ddd}
.search-label{position:absolute;left:19px;top:15px;font-size:13px;color:#555}
.search-input{position:absolute;left:19px;top:39px;width:442px;height:27px;border:1px solid #e0e0e0;background:#fff}
.search-input svg{position:absolute;right:8px;top:8px;width:11px;height:11px}
.search-divider{position:absolute;left:484px;top:37px;width:1px;height:31px;background:#ccc}
.advanced-link{position:absolute;left:501px;top:45px;font-size:11.5px;color:#9ac9c4;text-decoration:underline}
.filter-bar{position:absolute;left:0;top:92px;width:100%;height:45px;background:#f3f3f3}
.tag{position:absolute;top:11px;height:25px;background:var(--accent);color:#fff;font-size:10.5px;font-weight:700;display:flex;align-items:center;justify-content:space-between;padding:0 6px;border:1px solid #138f84}
.tag-state{left:17px;width:79px}
.tag-leg{left:104px;width:108px}
.filter{position:absolute;left:882px;top:16px;font-size:11.5px;color:#444;display:flex;align-items:center;gap:6px}
.view-toggle{position:absolute;left:971px;top:15px;display:flex;gap:7px}
.view-toggle span{width:17px;height:17px;border:2px solid #333;display:block}
.view-toggle span+span{border-color:#bbb}
.card{position:absolute;background:#fff;border:1px solid var(--card-line)}
.card-head{height:42px;background:linear-gradient(#f7f7f7,#e8e8e8);border-bottom:1px solid var(--card-line);display:flex;align-items:center;padding:0 16px 0 19px;gap:10px;font-size:15px;color:#555}
.card-head .tagicon{margin-left:auto;width:16px;height:16px;fill:#666}
.card-head .ic{width:18px;height:18px;fill:none;stroke:var(--brand);stroke-width:1.5}
.featured{left:28px;top:513px;width:1029px;height:322px}
.elections{position:absolute;left:18px;top:59px;width:993px;border-collapse:collapse;font-size:10.5px}
.elections th{background:var(--table-head);color:#fff;font-weight:500;height:29px}
.elections td{height:36px;text-align:center;color:#333}
.elections td:first-child{text-align:left;padding-left:19px}
.elections tr:nth-child(even) td{background:#f1f1f1}
.races{left:28px;top:854px;width:505px;height:269px}
.contributors{left:550px;top:854px;width:507px;height:269px}
.site-footer{position:absolute;left:0;top:1166px;width:1085px;height:34px;background:var(--footer);color:#ccc;font-size:11.5px;display:flex;align-items:center;justify-content:center}
</style>
</head>
<body>
<header class="site-header">
  <div class="brand">OPEN LEDGER</div>
  <div class="header-tools">
    <svg viewBox="0 0 16 16"><path d="M2 5h5v2H4v6h8v-3h2v5H2zM9 1h6v6l-2-2-4 4-2-2 4-4z"/></svg>
    <svg viewBox="0 0 16 16"><path d="M1 3h14v10H1zM2 4l6 5 6-5v1L8 10 2 5z" fill-rule="evenodd"/></svg>
    <svg viewBox="0 0 16 16"><path d="M8 1a4 4 0 014 4v5l2 2H2l2-2V5a4 4 0 014-4zM6 13h4a2 2 0 01-4 0z"/></svg>
  </div>
</header>
<nav class="main-nav">
  <a href="#">Overview</a><a href="#">Candidates</a><a href="#">PACs</a><a href="#">Parties</a><a href="#">Organizations</a><a href="#">IEs</a><a href="#">Propositions</a><a href="#">Individuals</a><a href="#">Vendors</a><a href="#">Advanced</a>
</nav>
<div class="nav-active"></div>
<div class="hero" role="img" aria-label="Blurred photo of smiling supporters waving small flags at a campaign rally"></div>

<section class="search-panel">
  <div class="search-label">Candidate Search</div>
  <div class="search-input"><svg viewBox="0 0 12 12"><circle cx="5" cy="5" r="3.5" fill="none" stroke="#aaa"/><path d="M7.5 7.5L11 11" stroke="#aaa"/></svg></div>
  <div class="search-divider"></div>
  <a class="advanced-link">Advanced Search</a>
  <div class="filter-bar">
    <div class="tag tag-state">State <span>✖</span></div>
    <div class="tag tag-leg">Legislature <span>✖</span></div>
    <div class="filter"><svg width="16" height="14" viewBox="0 0 16 14" stroke="#555" fill="#fff"><path d="M3 0v14M8 0v14M13 0v14"/><circle cx="3" cy="9" r="2"/><circle cx="8" cy="4" r="2"/><circle cx="13" cy="9" r="2"/></svg>FILTER</div>
    <div class="view-toggle"><span></span><span></span></div>
  </div>
</section>

<section class="card featured">
  <div class="card-head">
    <svg class="ic" viewBox="0 0 18 18"><circle cx="9" cy="6" r="4"/><path d="M2 17c0-4 3-6 7-6s7 2 7 6z"/></svg>
    Featured Elections
    <svg class="tagicon" viewBox="0 0 16 16"><path d="M1 2h6l7 7-5 5-8-7z"/><circle cx="4" cy="5" r="1" fill="#fff"/></svg>
  </div>
  <table class="elections">
    <colgroup><col style="width:148px"><col style="width:147px"><col style="width:131px"><col style="width:134px"><col style="width:135px"><col style="width:129px"><col style="width:169px"></colgroup>
    <tr><th>Name</th><th>Office</th><th>Party</th><th>Income</th><th>Expense</th><th>IE Setup</th><th>IE Opp</th></tr>
    <tr><td>HARTLEY, JUNE P</td><td>Rep Dist 15</td><td>Rep Private</td><td>$2,350</td><td>$1,012</td><td>$0</td><td>$0</td></tr>
    <tr><td>CORWIN, DALE ANTON</td><td>Rep Dist 26</td><td>Rep Private</td><td>$0</td><td>$15</td><td>$0</td><td>$0</td></tr>
    <tr><td>HARTLEY, JUNE P</td><td>Rep Dist 15</td><td>Rep Private</td><td>$2,350</td><td>$1,012</td><td>$0</td><td>$0</td></tr>
    <tr><td>CORWIN, DALE ANTON</td><td>Rep Dist 26</td><td>Rep Private</td><td>$0</td><td>$15</td><td>$0</td><td>$0</td></tr>
    <tr><td>HARTLEY, JUNE P</td><td>Rep Dist 15</td><td>Rep Private</td><td>$2,350</td><td>$1,012</td><td>$0</td><td>$0</td></tr>
    <tr><td>CORWIN, DALE ANTON</td><td>Rep Dist 26</td><td>Rep Private</td><td>$0</td><td>$15</td><td>$0</td><td>$0</td></tr>
  </table>
</section>

<section class="card races">
  <div class="card-head">
    <svg class="ic" viewBox="0 0 18 18"><circle cx="9" cy="9" r="6"/><circle cx="9" cy="7" r="2"/><path d="M5.5 13c1-2 6-2 7 0"/></svg>
    Races of Interest
    <svg class="tagicon" viewBox="0 0 16 16"><path d="M1 2h6l7 7-5 5-8-7z"/><circle cx="4" cy="5" r="1" fill="#fff"/></svg>
  </div>
  <svg width="505" height="226" viewBox="0 0 505 226" font-family="Roboto, sans-serif" font-size="10.5" text-anchor="middle">
    <g fill="none" stroke-width="14" transform="rotate(-90)">
      <circle cx="-65" cy="103" r="30" stroke="var(--lilac)" stroke-dasharray="120 189"/>
      <circle cx="-65" cy="103" r="30" stroke="var(--blue)" stroke-dasharray="0 120 30 189"/>
      <circle cx="-65" cy="103" r="30" stroke="var(--cyan)" stroke-dasharray="0 150 39 189"/>
      <circle cx="-65" cy="241" r="30" stroke="var(--cyan)" stroke-dasharray="40 189"/>
      <circle cx="-65" cy="241" r="30" stroke="var(--blue)" stroke-dasharray="0 40 30 189"/>
      <circle cx="-65" cy="241" r="30" stroke="var(--lilac)" stroke-dasharray="0 70 45 189"/>
      <circle cx="-65" cy="241" r="30" stroke="var(--cyan)" stroke-dasharray="0 115 74 189"/>
      <circle cx="-65" cy="380" r="30" stroke="var(--blue)" stroke-dasharray="0 25 135 189"/>
      <circle cx="-65" cy="380" r="30" stroke="var(--lilac)" stroke-dasharray="25 189"/>
      <circle cx="-65" cy="380" r="30" stroke="var(--cyan)" stroke-dasharray="0 160 29 189"/>
    </g>
    <g fill="#222">
      <text x="103" y="125" font-weight="500">BOB</text><text x="103" y="140">FOR SENATE</text>
      <text x="241" y="124" font-weight="500">MARK</text><text x="241" y="139">FOR SENATE</text>
      <text x="380" y="121" font-weight="500">COURTNEY</text><text x="380" y="136">FOR SENATE</text>
    </g>
    <g text-anchor="start" font-size="10" fill="#333">
      <rect x="178" y="187" width="8" height="8" fill="var(--cyan)"/><text x="190" y="195">Jan</text>
      <rect x="230" y="187" width="8" height="8" fill="var(--blue)"/><text x="240" y="195">Feb</text>
      <rect x="279" y="187" width="8" height="8" fill="var(--lilac)"/><text x="291" y="195">Mar</text>
    </g>
  </svg>
</section>

<section class="card contributors">
  <div class="card-head">
    <svg class="ic" viewBox="0 0 18 18"><circle cx="9" cy="7" r="5"/><circle cx="9" cy="7" r="2"/><path d="M6 11l-1 6 4-2 4 2-1-6"/></svg>
    Contributors of Interest
    <svg class="tagicon" viewBox="0 0 16 16"><path d="M1 2h6l7 7-5 5-8-7z"/><circle cx="4" cy="5" r="1" fill="#fff"/></svg>
  </div>
  <svg width="507" height="226" viewBox="0 0 507 226" font-family="Roboto, sans-serif" font-size="8.5" fill="#666">
    <line x1="102" y1="14" x2="102" y2="176" stroke="#ddd"/>
    <g text-anchor="end"><text x="96" y="34">$80000</text><text x="96" y="70">$60000</text><text x="96" y="106">$40000</text><text x="96" y="142">$20000</text><text x="96" y="177">$0</text></g>
    <text transform="translate(36 106) rotate(-90)" text-anchor="middle" font-size="9.5" fill="#999">Dollar on Amount</text>
    <path d="M103 139C150 120 170 55 210 53S250 155 277 155S370 110 421 65V174H103z" fill="#ececec"/>
    <path d="M103 139C125 140 135 145 150 135S170 104 187 104S250 176 277 176S320 104 350 104S400 150 421 159V174H103z" fill="var(--cyan)"/>
    <line x1="217" y1="45" x2="217" y2="114" stroke="#888" stroke-width=".7"/>
    <circle cx="217" cy="45" r="6" fill="#10b4ee"/>
    <line x1="392" y1="81" x2="392" y2="151" stroke="#888" stroke-width=".7"/>
    <circle cx="392" cy="81" r="6" fill="#10b4ee"/>
    <g font-size="10.5" fill="#333" text-anchor="middle"><text x="219" y="30">-3.05%</text><text x="395" y="67">-2.35%</text></g>
    <g text-anchor="middle" fill="#444"><text x="108" y="196">Jan</text><text x="159" y="196">Feb</text><text x="211" y="196">Mar</text><text x="262" y="196">Apr</text><text x="315" y="196">May</text><text x="366" y="196">Jun</text><text x="416" y="196">July</text></g>
    <text x="246" y="216" text-anchor="middle" font-size="9.5" fill="#aaa">Time in months</text>
  </svg>
</section>

<footer class="site-footer">Disclaimer &nbsp;|&nbsp; Copyright</footer>
</body>
</html>
```